Real estate agent website

I am a new real estate agent and in of a simple but powerful website that is linked to the local Multiple listing services (MLS). It should have a lending page that is connected to my customer relationship management (CRM) software. It must have an ability for potential customers to search for properties and be able to communicate with me easily.
Updates

Updates: The website themes must includes MLS-IDX integration with a grid layout and property slider so i can showcase featured properties. I also would like to have future where potential client can search and have alerts depending on a search criteria.

Industry/Entity Type

Real Estate

Coding

Coded - Design and coding required

Number of Pages Required

3 page

Requirements
Must have
• Home page, Resources page, About Me with contact me window page

```html
<!DOCTYPE html>
<html lang="en">
<head>
<meta charset="utf-8">
<title>Marisa Vance Realtor</title>
<link href="https://fonts.googleapis.com/css2?family=Montserrat:wght@500;600;700&family=Poppins:ital,wght@0,400;0,500;0,600;1,400&display=swap" rel="stylesheet">
<style>
:root{
  --gold:#b8903a;
  --gold-dark:#a57f2e;
  --ink:#1e1e1e;
  --text:#555;
  --muted:#8a8a8a;
  --navy:#25303f;
  --slate:#3f4c64;
  --light:#f3f2f0;
  --white:#fff;
}
*{box-sizing:border-box;margin:0;padding:0}
html,body{width:1200px;height:5240px;overflow:hidden}
body{position:relative;font-family:"Poppins",sans-serif;color:var(--text);background:var(--white)}
.abs{position:absolute}
.h2{font-family:"Montserrat",sans-serif;font-weight:600;color:var(--ink);font-size:38px;text-align:center;width:1200px;left:0}
.lead{font-size:15px;line-height:30px;text-align:center;width:1200px;left:0;color:var(--text)}
.btn{display:flex;align-items:center;justify-content:center;gap:6px;font-size:13px;font-weight:500;text-transform:uppercase;color:var(--white);background:var(--gold)}
.dot-ico{width:11px;height:11px;border-radius:50%;background:currentColor;display:inline-block}
.photo{position:absolute}
/* header */
.topbar{left:376px;top:0;width:824px;height:45px;background:var(--gold);clip-path:polygon(0 0,100% 0,100% 100%,40px 100%);display:flex;align-items:center;gap:22px;padding-left:60px;color:var(--white);font-size:16px}
.topbar .item{display:flex;align-items:center;gap:8px}
.circ{width:28px;height:28px;border:1.5px solid var(--white);border-radius:50%;display:inline-block}
.nav{top:66px;left:446px;display:flex;gap:48px;font-size:15px;font-weight:500;color:var(--ink)}
.logo{left:88px;top:6px;width:174px;height:150px;border-radius:50%;background:var(--white);border:3px solid var(--gold);display:flex;align-items:center;justify-content:center;text-align:center;font-family:"Montserrat",sans-serif;font-weight:600;color:var(--gold);font-size:17px;line-height:24px;z-index:3}
/* hero */
.hero{left:0;top:105px;width:1200px;height:623px;background:linear-gradient(120deg,#6b4a34,#a88a6e 40%,#e3e0da 65%,#545b63)}
.hero-box{left:88px;top:248px;width:420px;height:270px;background:rgba(0,0,0,.28)}
.hero-title{left:100px;top:252px;font-family:"Montserrat",sans-serif;font-weight:700;font-size:62px;line-height:58px;color:var(--white)}
.hero-text{left:100px;top:390px;font-size:15px;line-height:30px;color:var(--white);width:400px}
.hero-btn{left:100px;top:470px;width:180px;height:44px;background:var(--white);color:var(--gold)}
.search{left:142px;top:692px;width:912px;height:77px;background:var(--white);box-shadow:0 4px 14px rgba(0,0,0,.12);display:flex;align-items:center}
.search .f{height:52px;padding:0 32px;border-right:1px solid #ddd;font-size:12px;color:var(--ink)}
.search .f span{display:block;color:var(--muted);font-size:11px;text-transform:uppercase;margin-bottom:6px}
.search-go{left:980px;top:697px;width:68px;height:66px;background:var(--gold);display:flex;align-items:center;justify-content:center}
/* categories */
.cat-label{font-size:17px;font-weight:500;color:var(--ink);text-transform:uppercase}
/* about */
.about-bg{left:598px;top:1475px;width:602px;height:625px;background:var(--light)}
.about-text{left:659px;top:1610px;width:440px;font-size:15px;line-height:32.5px}
/* cards */
.card{background:var(--white);box-shadow:0 4px 12px rgba(0,0,0,.12)}
.price{font-size:19px;font-weight:600;color:var(--ink)}
.meta{font-size:14px;color:var(--text)}
.arrow{width:40px;height:40px;border:1.5px solid #777;border-radius:50%;display:flex;align-items:center;justify-content:center}
/* testimonials */
.testi{left:0;top:2854px;width:1200px;height:543px;background:linear-gradient(135deg,#46536b,#34405a 60%,#4a5770)}
.t-card{width:407px;height:246px;background:var(--white);border-radius:14px;padding:22px 18px 0 18px}
.t-quote{font-style:italic;font-size:14px;line-height:28px;color:var(--text)}
.avatar{width:102px;height:102px;border-radius:50%;border:4px solid var(--white);background:linear-gradient(#b9a38e,#6d5b4f)}
.stars{color:var(--gold);font-size:18px;letter-spacing:1px}
/* blog */
.blog-date{font-size:13px;color:var(--ink)}
.blog-title{font-size:16px;font-weight:500;color:var(--ink);line-height:26px}
.blog-text{font-size:13px;line-height:22px;color:var(--muted)}
.more{font-size:14px;font-weight:600;color:var(--gold);text-decoration:underline}
/* contact */
.field{height:45px;border:1px solid #c8c8c8;color:var(--white);font-size:14px;padding:12px 14px}
/* footer */
.fhead{font-size:15px;font-weight:600;color:var(--ink);text-transform:uppercase}
.flist{font-size:14px;line-height:25px;color:var(--ink)}
.ficon{width:32px;height:32px;border:1.5px solid var(--gold);border-radius:50%;display:flex;align-items:center;justify-content:center}
</style>
</head>
<body>

<header>
  <div class="abs topbar">
    <div class="item"><span class="circ"></span>+1 888-888-8888</div>
    <div class="item"><span class="circ"></span>hello@vancehomes.example</div>
    <div class="item" style="gap:6px"><span class="circ"></span><span class="circ"></span><span class="circ"></span><span class="circ"></span></div>
  </div>
  <div class="abs logo">Marisa Vance<br>Realtor</div>
  <nav class="abs nav"><span>HOME</span><span>ABOUT US</span><span>SERVICES</span><span>PROPERTIES</span><span>BLOG</span><span>CONTACT US</span></nav>
</header>

<section>
  <div class="abs hero" role="img" aria-label="Bright open-plan living room and kitchen with wooden floor"></div>
  <div class="abs hero-box"></div>
  <h1 class="abs hero-title">REAL ESTATE<br>AGENT</h1>
  <p class="abs hero-text">Lorem ipsum dolor sit amet, consectetur adipiscing elit, sed do eiusmod tempor incididunt</p>
  <div class="abs btn hero-btn">All properties <span class="dot-ico"></span></div>
  <div class="abs search">
    <div class="f" style="width:230px"><span>Search by reference</span>Keywords</div>
    <div class="f" style="width:165px"><span>Regions</span>Select</div>
    <div class="f" style="width:212px"><span>Type</span>Apartments &nbsp;&nbsp;&nbsp;⌄</div>
    <div class="f" style="border:0;width:240px"><span>Price range</span>1-54,000,000 USD ⌄</div>
  </div>
  <div class="abs search-go"><svg width="34" height="34" viewBox="0 0 34 34" fill="none" stroke="#fff" stroke-width="2.5"><circle cx="14" cy="14" r="10"/><line x1="21" y1="21" x2="31" y2="31"/></svg></div>
</section>

<section>
  <h2 class="abs h2" style="top:852px">CATEGORIES</h2>
  <p class="abs lead" style="top:900px">At vero eos et accusamus et iusto odio dignissimos ducimus qui blanditiis<br>praentium voluptatum deleniti atque corrupti</p>
  <div class="photo" style="left:100px;top:985px;width:238px;height:290px;background:linear-gradient(#cfe0ee,#e8e8e6 55%,#4fa9c4)" role="img" aria-label="Modern white villa with pool"></div>
  <div class="photo" style="left:354px;top:985px;width:238px;height:290px;background:linear-gradient(#6b7278,#a09a90 60%,#55595c)" role="img" aria-label="Grey living room with fireplace"></div>
  <div class="photo" style="left:608px;top:985px;width:238px;height:290px;background:linear-gradient(#d9d3c6,#b7ab98 60%,#8d8476)" role="img" aria-label="Cosy bedroom with warm cushions"></div>
  <div class="photo" style="left:862px;top:985px;width:238px;height:290px;background:linear-gradient(#bcd8ea,#e9ece9 55%,#6ec3d4)" role="img" aria-label="Holiday house with turquoise pool"></div>
  <div class="abs cat-label" style="left:100px;top:1286px">Luxury places</div>
  <div class="abs cat-label" style="left:354px;top:1286px">Waterfront</div>
  <div class="abs cat-label" style="left:608px;top:1286px">Alps</div>
  <div class="abs cat-label" style="left:862px;top:1286px">Holiday rentals</div>
</section>

<section>
  <div class="abs about-bg"></div>
  <div class="photo" style="left:0;top:1400px;width:598px;height:624px;background:linear-gradient(90deg,#c6c9cc,#e9e7e2 50%,#b7b5b0)" role="img" aria-label="Agent showing a happy couple around a home"></div>
  <h2 class="abs" style="left:659px;top:1553px;font-family:Montserrat,sans-serif;font-weight:600;font-size:38px;color:var(--ink)">ABOUT US</h2>
  <p class="abs about-text">At vero eos et acmus et iusto odio dignissimos ducimus qui blanditiis praesentium tatum deleniti atque corrupti quos dolores et quas molestias excepturi sint occaecati cupiditate non provident, similie sunt in culpa qui officia deserunt mollitia animi, id est laborum et dolorum fuga. Et harum quidem rerum facilis est et expedita distinctio. Nam libero tempore, cum sluta nobis est eligendi optio cumque nihil impedit quo</p>
  <div class="abs btn" style="left:653px;top:1896px;width:182px;height:42px">All properties <span class="dot-ico"></span></div>
</section>

<section>
  <h2 class="abs h2" style="top:2184px">FEATURED PROPERTIES</h2>
  <p class="abs lead" style="top:2232px">At vero eos et accusamus et iusto odio dignissimos ducimus qui blanditiis<br>praentium voluptatum deleniti atque corrupti</p>
  <div class="abs arrow" style="left:43px;top:2496px"><svg width="14" height="14" viewBox="0 0 14 14" fill="none" stroke="#555" stroke-width="1.8"><polyline points="9,2 4,7 9,12"/></svg></div>
  <div class="abs arrow" style="left:1117px;top:2496px"><svg width="14" height="14" viewBox="0 0 14 14" fill="none" stroke="#555" stroke-width="1.8"><polyline points="5,2 10,7 5,12"/></svg></div>

  <div class="photo" style="left:100px;top:2321px;width:317px;height:374px;background:linear-gradient(#7fb0dc,#b9cbdb 45%,#3f5672)" role="img" aria-label="Blue two-storey house"></div>
  <div class="photo" style="left:441px;top:2321px;width:318px;height:374px;background:linear-gradient(#1f6fc4,#6aa3dc 40%,#e8ecef 70%,#8a8f8a)" role="img" aria-label="White modern apartment building"></div>
  <div class="photo" style="left:783px;top:2321px;width:317px;height:374px;background:linear-gradient(#a9c6d7,#cfd6d6 45%,#8fa06f)" role="img" aria-label="Classic house with wide porch"></div>

  <div class="abs card" style="left:116px;top:2650px;width:285px;height:110px;padding:14px 14px"><div class="price">$208,724</div><div class="meta" style="margin-top:8px">2beds | 1ba | 2502 sft.n</div><div class="meta" style="margin-top:8px;display:flex;gap:8px;align-items:center"><svg width="14" height="18" viewBox="0 0 14 18"><path d="M7 0a7 7 0 0 0-7 7c0 5 7 11 7 11s7-6 7-11a7 7 0 0 0-7-7z" fill="#d0312d"/><circle cx="7" cy="7" r="2.5" fill="#fff"/></svg>1234 Main Rd Somewhere 12345</div></div>
  <div class="abs card" style="left:457px;top:2650px;width:286px;height:110px;padding:14px 14px"><div class="price">$208,724</div><div class="meta" style="margin-top:8px">2beds | 1ba | 2502 sft.n</div><div class="meta" style="margin-top:8px;display:flex;gap:8px;align-items:center"><svg width="14" height="18" viewBox="0 0 14 18"><path d="M7 0a7 7 0 0 0-7 7c0 5 7 11 7 11s7-6 7-11a7 7 0 0 0-7-7z" fill="#d0312d"/><circle cx="7" cy="7" r="2.5" fill="#fff"/></svg>1234 Main Rd Somewhere 12345</div></div>
  <div class="abs card" style="left:799px;top:2650px;width:285px;height:110px;padding:14px 14px"><div class="price">$208,724</div><div class="meta" style="margin-top:8px">2beds | 1ba | 2502 sft.n</div><div class="meta" style="margin-top:8px;display:flex;gap:8px;align-items:center"><svg width="14" height="18" viewBox="0 0 14 18"><path d="M7 0a7 7 0 0 0-7 7c0 5 7 11 7 11s7-6 7-11a7 7 0 0 0-7-7z" fill="#d0312d"/><circle cx="7" cy="7" r="2.5" fill="#fff"/></svg>1234 Main Rd Somewhere 12345</div></div>
</section>

<section>
  <div class="abs testi" role="img" aria-label="Dark blue backdrop of glass towers"></div>
  <h2 class="abs h2" style="top:2923px;color:var(--white)">WHAT OUR CLIENTS SAY</h2>
  <svg class="abs" style="left:128px;top:3130px" width="26" height="16" viewBox="0 0 26 16" fill="none" stroke="#fff" stroke-width="1.6"><polyline points="8,1 1,8 8,15"/><line x1="1" y1="8" x2="25" y2="8"/></svg>
  <svg class="abs" style="left:1046px;top:3130px" width="26" height="16" viewBox="0 0 26 16" fill="none" stroke="#fff" stroke-width="1.6"><polyline points="18,1 25,8 18,15"/><line x1="1" y1="8" x2="25" y2="8"/></svg>

  <div class="abs t-card" style="left:179px;top:3029px">
    <div style="margin-left:110px"><div class="stars">★★★★★</div><div style="font-size:15px;font-weight:600;color:var(--ink);margin-top:6px">Daniel Ortis</div><div style="font-size:12px;color:var(--muted)">Owner, Summit Drywall</div></div>
    <p class="t-quote" style="margin-top:22px"><span style="color:#bbb;font-size:26px;font-style:normal">“</span> your efforts and persistance paid off for the both of us. While it may have taken over one year to find the right business for me, in the end it was well worth the wait.</p>
  </div>
  <div class="abs avatar" style="left:177px;top:3004px" role="img" aria-label="Client portrait"></div>

  <div class="abs t-card" style="left:616px;top:3029px">
    <div style="margin-left:110px"><div class="stars">★★★★★</div><div style="font-size:15px;font-weight:600;color:var(--ink);margin-top:6px">Lena and Paul Hartwell</div><div style="font-size:12px;color:var(--muted)">Owner, Maple Court Residence</div></div>
    <p class="t-quote" style="margin-top:22px"><span style="color:#bbb;font-size:26px;font-style:normal">“</span> the effort you put forth to help us throughout the whole buying process was unexpected, way beyond the call of duty and very much appreciated. Your customer service was second to none!</p>
  </div>
  <div class="abs avatar" style="left:614px;top:3004px" role="img" aria-label="Client portrait"></div>

  <div class="abs" style="left:564px;top:3302px;display:flex;gap:6px"><span style="width:9px;height:9px;border-radius:50%;background:#fff"></span><span style="width:9px;height:9px;border-radius:50%;border:1px solid #fff"></span><span style="width:9px;height:9px;border-radius:50%;border:1px solid #fff"></span><span style="width:9px;height:9px;border-radius:50%;border:1px solid #fff"></span><span style="width:9px;height:9px;border-radius:50%;border:1px solid #fff"></span></div>
</section>

<section>
  <h2 class="abs h2" style="top:3484px">LATEST BLOG</h2>
  <div class="photo" style="left:100px;top:3554px;width:317px;height:234px;background:linear-gradient(#5d6670,#8c8c88 50%,#3b3f46)" role="img" aria-label="Colleagues discussing a tablet"></div>
  <div class="photo" style="left:441px;top:3554px;width:318px;height:234px;background:linear-gradient(#e3e0d8,#c9c2b2 55%,#6f6a63)" role="img" aria-label="Business handshake at a meeting"></div>
  <div class="photo" style="left:783px;top:3554px;width:317px;height:234px;background:linear-gradient(#aac5d8,#d9ddd9 50%,#7e8a90)" role="img" aria-label="Agent meeting a couple on a terrace"></div>

  <div class="abs card" style="left:116px;top:3749px;width:285px;height:218px;padding:12px 16px"><div class="blog-date" style="display:flex;gap:10px;align-items:center"><svg width="24" height="20" viewBox="0 0 24 20" fill="none" stroke="var(--gold)" stroke-width="1.5"><rect x="1" y="3" width="22" height="16"/><line x1="1" y1="8" x2="23" y2="8"/></svg>November 14, 2021</div><div class="blog-title" style="margin-top:10px">The standard Lorem I passage, used since the 1500s</div><p class="blog-text" style="margin-top:8px">At vero eos et accusamus et iusto odio dignissimos ducimus qui blanditiis proesentium voluptatum</p><div class="more" style="margin-top:10px">READ MORE</div></div>
  <div class="abs card" style="left:457px;top:3749px;width:286px;height:218px;padding:12px 16px"><div class="blog-date" style="display:flex;gap:10px;align-items:center"><svg width="24" height="20" viewBox="0 0 24 20" fill="none" stroke="var(--gold)" stroke-width="1.5"><rect x="1" y="3" width="22" height="16"/><line x1="1" y1="8" x2="23" y2="8"/></svg>November 14, 2021</div><div class="blog-title" style="margin-top:10px">The standard Lorem I passage, used since the 1500s</div><p class="blog-text" style="margin-top:8px">At vero eos et accusamus et iusto odio dignissimos ducimus qui blanditiis proesentium voluptatum</p><div class="more" style="margin-top:10px">READ MORE</div></div>
  <div class="abs card" style="left:799px;top:3749px;width:285px;height:218px;padding:12px 16px"><div class="blog-date" style="display:flex;gap:10px;align-items:center"><svg width="24" height="20" viewBox="0 0 24 20" fill="none" stroke="var(--gold)" stroke-width="1.5"><rect x="1" y="3" width="22" height="16"/><line x1="1" y1="8" x2="23" y2="8"/></svg>November 14, 2021</div><div class="blog-title" style="margin-top:10px">The standard Lorem I passage, used since the 1500s</div><p class="blog-text" style="margin-top:8px">At vero eos et accusamus et iusto odio dignissimos ducimus qui blanditiis proesentium voluptatum</p><div class="more" style="margin-top:10px">READ MORE</div></div>
</section>

<section>
  <div class="photo" style="left:0;top:4062px;width:592px;height:521px;background:linear-gradient(135deg,#ececec,#e2e4e6 50%,#eeeeee)" role="img" aria-label="Street map around the office location"></div>
  <div class="abs" style="left:592px;top:4062px;width:608px;height:521px;background:var(--navy)"></div>
  <h2 class="abs" style="left:669px;top:4133px;font-family:Montserrat,sans-serif;font-weight:600;font-size:38px;color:var(--white)">CONTACT US</h2>
  <div class="abs" style="left:669px;top:4184px;width:54px;height:3px;background:var(--gold)"></div>
  <div class="abs field" style="left:669px;top:4212px;width:234px">Name</div>
  <div class="abs field" style="left:913px;top:4212px;width:234px">Email</div>
  <div class="abs field" style="left:669px;top:4271px;width:234px">Phone</div>
  <div class="abs field" style="left:913px;top:4271px;width:234px">Subject</div>
  <div class="abs field" style="left:669px;top:4328px;width:478px;height:112px">Message</div>
  <div class="abs btn" style="left:669px;top:4457px;width:152px;height:38px">Submit <span class="dot-ico"></span></div>
</section>

<section>
  <div class="abs" style="left:0;top:4583px;width:1200px;height:319px;background:linear-gradient(90deg,#b0893a,#c29a45 50%,#b0893a)"></div>
  <p class="abs" style="left:0;top:4662px;width:1200px;text-align:center;font-family:Montserrat,sans-serif;font-weight:600;font-size:32px;line-height:42px;color:var(--white)">Call us today and For a Free Confidential<br>Consultation, Call Real estate agent</p>
  <div class="abs btn" style="left:427px;top:4770px;width:163px;height:41px;background:transparent;border:1.5px solid var(--white)">Call us today</div>
  <div class="abs btn" style="left:610px;top:4770px;width:161px;height:41px;background:#111">Get started</div>
</section>

<footer>
  <div class="abs logo" style="left:136px;top:4932px;width:224px;height:224px;font-size:21px;line-height:30px">Marisa Vance<br>Realtor</div>
  <div class="abs" style="left:445px;top:4955px"><div class="fhead">Quick links</div><div class="flist" style="margin-top:10px">› Home<br>› About<br>› Services<br>› Properties<br>› Blog<br>› Contact</div></div>
  <div class="abs" style="left:635px;top:4955px"><div class="fhead">Useful links</div><div class="flist" style="margin-top:10px">› Lorem Ipsum passage<br>› Sed ut perspiciatis<br>› At vero eos et accusa<br>› Dolor sit ame</div></div>
  <div class="abs" style="left:869px;top:4955px"><div class="fhead">Contact details</div>
    <div class="flist" style="margin-top:14px;display:flex;gap:14px;align-items:center;line-height:21px"><span class="ficon"><svg width="12" height="16" viewBox="0 0 14 18"><path d="M7 0a7 7 0 0 0-7 7c0 5 7 11 7 11s7-6 7-11a7 7 0 0 0-7-7z" fill="var(--gold)"/></svg></span>1234 Main Rd<br>Somewhere, US 12345</div>
    <div class="flist" style="margin-top:10px;display:flex;gap:14px;align-items:center"><span class="ficon"><svg width="14" height="14" viewBox="0 0 14 14"><path d="M3 1l3 3-2 2c1 2 2 3 4 4l2-2 3 3-2 2C6 13 1 8 1 3z" fill="var(--gold)"/></svg></span>+1 888-888-8888</div>
    <div class="flist" style="margin-top:10px;display:flex;gap:14px;align-items:center"><span class="ficon"><svg width="14" height="10" viewBox="0 0 14 10" fill="none" stroke="var(--gold)" stroke-width="1.5"><rect x="1" y="1" width="12" height="8"/><polyline points="1,1 7,6 13,1"/></svg></span>hello@vancehomes.example</div>
  </div>
  <div class="abs" style="left:0;top:5178px;width:1200px;height:62px;background:var(--light)"></div>
  <div class="abs" style="left:100px;top:5199px;font-size:14px;color:var(--ink)">© 2023 The Harbor Crest Group . All Rights Reserved.</div>
  <div class="abs" style="left:880px;top:5191px;display:flex;gap:8px"><span style="width:36px;height:36px;border-radius:50%;background:var(--gold)"></span><span style="width:36px;height:36px;border-radius:50%;background:var(--gold)"></span><span style="width:36px;height:36px;border-radius:50%;background:var(--gold)"></span><span style="width:36px;height:36px;border-radius:50%;background:var(--gold)"></span><span style="width:36px;height:36px;border-radius:50%;background:var(--gold)"></span></div>
</footer>

</body>
</html>
```